A gateway to the eyes of potential Tenlar Candidates and Clients

We are looking for a brochure that will grab attention, all most along the lines of an infogram. The business supplies people to the construction sector. So we want it simple but sharp.

I would like the brochure to be able to have a half fold effect when printed but the main focus will be to use it in an e-brochure format.

Main pages will be as follows:

About Us: Which will have a bit about the management team and some pictures.

Services: information for both candidate and clients.

Why us?:

Contact: Location, contact numbers etc.

FOR CONTENTS:
website will give you the content required. www.tenlarconstruction.co.uk
Updates

Project Deadline Extended Reason: Project was moved from a flyer to a brochure and the logo didn't upload. So I will be uploading my new logo and it will give additional time to get designs in. Cheers Added Monday, June 20, 2016

Target Market(s)

Clients and candidates for the construction market

Industry/Entity Type

Business

Requirements
Must have
• Bold and strong images of the construction sector. A simple to read format. Also needs to look good in an electronic format.
Nice to have
• I like the idea of a black and white model but with certain parts of the images highlighted in our colours.
Should not have
• Too much of a complex lay out.

```html
<!DOCTYPE html>
<html lang="en">
<head>
<meta charset="utf-8">
<title>Tenlar Construction – About Us</title>
<link rel="stylesheet" href="https://fonts.googleapis.com/css2?family=Exo:wght@700&family=Open+Sans:wght@300;400;600&display=swap">
<style>
  :root{
    --canvas:#e4e6e9;
    --page:#f7f7f7;
    --blue:#0a7cc1;
    --blue-deep:#0b5a9a;
    --blue-bright:#1a9ee0;
    --orange:#f39a1e;
    --text:#333a40;
    --muted:#4a5157;
    --white:#ffffff;
    --yellow:#f5c518;
  }
  *{box-sizing:border-box;margin:0;padding:0}
  html,body{width:1200px;height:800px;overflow:hidden;background:var(--canvas)}
  .canvas{position:relative;width:1200px;height:800px}
  .page{
    position:absolute;left:307px;top:1px;width:586px;height:798px;
    background:var(--page);box-shadow:0 2px 10px rgba(0,0,0,.15);
    font-family:"Open Sans",Arial,sans-serif;color:var(--text);
  }
  .section-tab{position:absolute;left:42px;top:40px;width:68px;height:28px}
  .section-tab span{
    position:absolute;left:12px;top:0;line-height:30px;
    font-family:"Exo",sans-serif;font-weight:700;font-size:22px;color:var(--white);
  }
  .hero-photo{
    position:absolute;left:42px;top:68px;width:496px;height:270px;
    background:linear-gradient(135deg,#c9d8ee 0%,#8eaad4 45%,#4a72b0 100%);
  }
  .hero-rule{position:absolute;left:42px;top:344px;width:496px;height:13px}
  .page-title{
    position:absolute;left:42px;top:394px;
    font-family:"Exo",sans-serif;font-weight:700;font-size:29px;letter-spacing:.5px;
    color:var(--blue);
  }
  .page-title .accent{color:var(--orange)}
  .tagline{
    position:absolute;left:42px;top:462px;width:496px;
    font-weight:300;font-size:17.5px;line-height:23px;color:var(--muted);
  }
  .body-copy{
    position:absolute;left:42px;width:496px;
    font-size:9.4px;line-height:14px;color:var(--text);text-align:justify;
  }
  .body-copy.intro{top:545px}
  .body-copy.second{top:635px}
  .drop-cap{
    float:left;font-size:62px;line-height:50px;margin:2px 6px 0 0;
    font-weight:400;color:var(--text);
  }
  .page-footer{
    position:absolute;left:0;bottom:0;width:586px;height:41px;
    background:linear-gradient(90deg,var(--blue-bright) 0%,var(--blue) 40%,var(--blue-deep) 100%);
  }
  .page-number{
    position:absolute;left:22px;top:12px;width:24px;height:18px;
    border:1.5px solid var(--white);color:var(--white);
    font-size:11px;font-weight:600;text-align:center;line-height:15px;
  }
  .web-address{
    position:absolute;right:32px;top:0;line-height:41px;
    color:var(--white);font-size:10.5px;font-weight:600;
  }
  .web-address::before{
    content:"";display:inline-block;width:9px;height:9px;border-radius:50%;
    background:var(--yellow);margin-right:8px;vertical-align:-1px;
  }
</style>
</head>
<body>
<div class="canvas">
  <article class="page">
    <svg class="section-tab" viewBox="0 0 68 28" aria-hidden="true">
      <polygon points="0,0 52,0 68,28 0,28" fill="var(--orange)"/>
    </svg>
    <div class="section-tab"><span>01</span></div>

    <div class="hero-photo" role="img" aria-label="Hard hat and folding rulers lying on rolled construction blueprints"></div>

    <svg class="hero-rule" viewBox="0 0 496 13" aria-hidden="true">
      <rect x="0" y="0" width="496" height="7" fill="var(--blue-deep)"/>
      <polygon points="12,7 28,7 20,13" fill="var(--blue-deep)"/>
    </svg>

    <h1 class="page-title">ABOUT <span class="accent">US</span></h1>

    <p class="tagline">Fresh start? New Job? Brighter Future? A Better you? Tenlar Construction is in your corner.</p>

    <p class="body-copy intro"><span class="drop-cap">E</span>stablished in 2016, Tenlar Construction has already been recognised as a market-leading specialist for contract and permanent recruitment both domestically and internationally. Our core focus is on delivering professional people into the following key areas, Project, Design, Surveying and we also deliever hand picked teams for the trades and labour.&nbsp; Due to our partnerships around Europe we have access to a huge pool of skilled candidates from the far reaches of Europe.</p>

    <p class="body-copy second">Our success is down to the dedicated consultants that offer a combination of well proactive approach and the ability to source candidates that are passive in the market place. Each one of them is experienced in their field and trained in executive search and selction methodology. That means you'll only ever deal with someone who has a thorough understanding of their candidates' and clients' needs. Add in our ethos of 'Innovation, Motivation, Dedication, as well as our core values of hard work and professionalism and the result is a genuine ability to deliver a truly dynamic recruitment service.</p>

    <footer class="page-footer">
      <div class="page-number">02</div>
      <div class="web-address">www.tenlarconstruction.co.uk</div>
    </footer>
  </article>
</div>
</body>
</html>
```